Bring me business with this creative business card

Design my new business card. I am looking for something different with an impact. People will take a look at this card & they will 1- see how different & creative I am, 2-understand what I do 3- Call me to meet me!

I make videos with a message, testimonials. I am dynamic, fun, creative & human. My new website is in construction but in the meantime you can check this old one: brightpath.ca & another one Fernquill.com & fernquill facebook page.
I make videos. sometimes with a cameraman, sometimes with my phone. As an ex Public Relations agent, the message is the most important thing for me. I want to make my clients shine! When they start with me they often remind me of a lamb, when I finish coaching them they are powerful like LIONS! That's why I need a powerful business card!

Target Market(s)

Entrepreneurs, solo entrepreneurs, small & medium companies & start ups. People i will meet while networking. People that need videos on their website & social Networks to get attention, to be visible. men & women. From 35 to 49 years old.
I am an ex Public relations agent. I used to send clients in traditional medias, now with videos they have more chances to be seen on google the new media. I do videos of the president, his team, his loyal clients saying how great the company is & expert videos like series so people can be seen for example every 1 st of every month with a short 2 minute video. Also with my 20 years in marketing & communications I can coach & give tips to anybody who needs it.
Target: anybody who would like my old website brightpath.ca & I also have another website but it will be off line soon: fernquill.com could give you ideas.

Industry/Entity Type

Communications

Contact Information for Business Card

I am in Montreal,So the business cards have to be the usual size like we have in Montreal: 9 cm x 5 cm
Details:My text: Corinne Vautrin Communication Coach/Story Lead. "SHARING STORIES THAT SOUND LIKE YOU" off: 514-555-0147 cell: 514-555-0183. fernquill.com
corinne@fernquill.com logo facebook, youtube, instagram

Colors
f37122

Requirements
Must have
• Dynamic, happy. Orange. Be creative in the look but NOT the shape of the card. Easy to read. Big enough to read.
Should not have
• No funny shapes: no round, no square, just the usual. I love creative but NOT on shape.

```html
<!DOCTYPE html>
<html lang="en">
<head>
<meta charset="utf-8">
<title>Fernquill business card</title>
<link rel="stylesheet" href="https://fonts.googleapis.com/css2?family=Cinzel:wght@700&family=Open+Sans:wght@400&display=swap">
<style>
  :root {
    --backdrop: #2b2624;
    --card: #0d0d0d;
    --orange: #f37122;
    --gold: #f5a41c;
    --amber: #fbbf2a;
    --text-grey: #c9c9c9;
    --rule: #3a3a3a;
  }
  * { box-sizing: border-box; margin: 0; padding: 0; }
  html, body { width: 1200px; height: 844px; overflow: hidden; background: var(--backdrop); }
  .stage { position: relative; width: 1200px; height: 844px; }
  .card {
    position: absolute; top: 278px; width: 520px; height: 289px;
    background: var(--card); box-shadow: 0 10px 30px rgba(0,0,0,.5);
  }
  .card--contact { left: 50px; }
  .card--brand { left: 630px; }

  /* contact side */
  .brand-mark {
    position: absolute; left: 40px; top: 62px; width: 150px;
    display: flex; flex-direction: column; align-items: center; gap: 12px;
  }
  .brand-mark__dot {
    width: 96px; height: 96px; border-radius: 50%;
    background: radial-gradient(circle at 50% 55%, var(--amber), var(--orange));
  }
  .brand-mark__name {
    font-family: "Cinzel", serif; font-weight: 700; font-size: 17px;
    color: var(--gold); letter-spacing: 1px;
  }
  .divider { position: absolute; left: 225px; top: 42px; width: 1px; height: 176px; background: var(--rule); }
  .person { position: absolute; left: 246px; top: 48px; }
  .person__name {
    font-family: "Cinzel", serif; font-weight: 700; font-size: 20px;
    color: var(--gold); letter-spacing: 1px; line-height: 1;
  }
  .person__title {
    font-family: "Open Sans", sans-serif; font-size: 11.5px; color: var(--text-grey); margin-top: 4px;
  }
  .contact-list { list-style: none; margin-top: 12px; }
  .contact-list li {
    display: flex; align-items: center; gap: 8px; height: 16px;
    font-family: "Open Sans", sans-serif; font-size: 12.5px; color: var(--text-grey);
  }
  .contact-list svg { width: 10px; height: 10px; flex: none; fill: var(--gold); }
  .tagline {
    position: absolute; left: 0; right: 0; bottom: 30px; text-align: center;
    font-family: "Cinzel", serif; font-weight: 700; font-size: 15px;
    color: var(--orange); letter-spacing: .5px;
  }

  /* brand side */
  .brand-lockup {
    position: absolute; inset: 0; display: flex; flex-direction: column;
    align-items: center; justify-content: center; gap: 10px;
  }
  .brand-lockup__dot {
    width: 104px; height: 104px; border-radius: 50%;
    background: radial-gradient(circle at 50% 55%, var(--amber), var(--orange));
  }
  .brand-lockup__name {
    font-family: "Cinzel", serif; font-weight: 700; font-size: 34px;
    color: var(--orange); letter-spacing: 1px; line-height: 1; margin-top: 8px;
  }
  .brand-lockup__motto {
    display: flex; align-items: center; gap: 8px;
    font-family: "Open Sans", sans-serif; font-size: 12px; color: var(--orange); letter-spacing: .5px;
  }
  .brand-lockup__motto::before, .brand-lockup__motto::after {
    content: ""; width: 50px; height: 1px; background: var(--orange);
  }
</style>
</head>
<body>
<main class="stage">
  <section class="card card--contact">
    <div class="brand-mark">
      <span class="brand-mark__dot"></span>
      <span class="brand-mark__name">FERNQUILL</span>
    </div>
    <div class="divider"></div>
    <div class="person">
      <h1 class="person__name">CORINNE V</h1>
      <p class="person__title">Communication Coach/Story Lead</p>
      <ul class="contact-list">
        <li><svg viewBox="0 0 10 10"><path d="M1 3c0-1 1-2 2-2h4c1 0 2 1 2 2v1H7V3H3v1H1z M2 5h6l1 4H1z"/></svg>514-555-0147</li>
        <li><svg viewBox="0 0 10 10"><path d="M3 0h4a1 1 0 0 1 1 1v8a1 1 0 0 1-1 1H3a1 1 0 0 1-1-1V1a1 1 0 0 1 1-1zm0 1.5v6h4v-6z"/></svg>514-555-0183</li>
        <li><svg viewBox="0 0 10 10"><path d="M0 2h10v6H0z M0 2l5 3.5L10 2" stroke="#0d0d0d" stroke-width=".8"/></svg>corinne@fernquill.com</li>
        <li><svg viewBox="0 0 10 10"><circle cx="5" cy="5" r="4.5"/><path d="M.5 5h9M5 .5c-2 2.5-2 6.5 0 9M5 .5c2 2.5 2 6.5 0 9" stroke="#0d0d0d" stroke-width=".7" fill="none"/></svg>www.fernquill.com</li>
      </ul>
    </div>
    <p class="tagline">SHARING STORIES THAT SOUND LIKE YOU</p>
  </section>

  <section class="card card--brand">
    <div class="brand-lockup">
      <span class="brand-lockup__dot"></span>
      <span class="brand-lockup__name">FERNQUILL</span>
      <span class="brand-lockup__motto">ONE STORY, ONE VOICE</span>
    </div>
  </section>
</main>
</body>
</html>
```